Email Banner for Technology Company

We need a new email banner. The purpose of the email banner is to make us look more professional as a business and keep all communications with clients uniform. The previous designs which we have included below have now become outdated as our brand has developed and we need the new banner to become more aligned and modern.
We are a marketing organization that specialises in lead generation, email newsletters are sent to prospects on a regular basis. Therefore, it is important that we have an aesthetically pleasing banner as this is the first real impression prospects have our business. First impressions matter.
We are looking for a new email banner design as the current design is now outdated and does not reflect who we are as a business.
The new banners are required for launch at the start of Q2.
There is future work in the pipeline for the winning design. We have multiple industry sites that will require the new design as well as creating each of these in multiple languages.
The design must include the Lumenfield Dossiers wording the tagline 'The Technology Pro’s Research Hub'.
It needs to be creative and fun but still remain professional, sticking with the colour theme that already exists.

```html
<!DOCTYPE html>
<html lang="en">
<head>
<meta charset="UTF-8">
<title>Lumenfield Dossiers – Email Banner</title>
<link rel="stylesheet" href="https://fonts.googleapis.com/css2?family=Montserrat:wght@500&display=swap">
<style>
  :root {
    --backdrop: #e8e8e8;
    --brand-blue: #0096d6;
    --white: #ffffff;
    --white-soft: rgba(255, 255, 255, 0.9);
    --white-clear: rgba(255, 255, 255, 0);
  }
  * { margin: 0; padding: 0; box-sizing: border-box; }
  html, body {
    width: 1200px;
    height: 323px;
    overflow: hidden;
    background: var(--backdrop);
  }
  .canvas {
    position: relative;
    width: 1200px;
    height: 323px;
  }
  .banner {
    position: absolute;
    left: 58px;
    top: 69px;
    width: 1076px;
    height: 178px;
    background: var(--brand-blue);
    overflow: hidden;
    font-family: "Montserrat", sans-serif;
    color: var(--white);
  }
  .decor {
    position: absolute;
  }
  .decor-left {
    left: 0;
    top: 0;
    width: 60px;
    height: 178px;
    background: linear-gradient(90deg, var(--white-soft), var(--white-clear));
  }
  .decor-top {
    left: 760px;
    top: 0;
    width: 190px;
    height: 12px;
    background: linear-gradient(180deg, var(--white-soft), var(--white-clear));
  }
  .decor-right {
    right: 0;
    top: 0;
    width: 80px;
    height: 130px;
    background: linear-gradient(270deg, var(--white-soft), var(--white-clear));
  }
  .brand {
    position: absolute;
    left: 45px;
    top: 56px;
    display: flex;
    align-items: center;
    gap: 14px;
    font-weight: 500;
    font-size: 50px;
    line-height: 1;
    letter-spacing: -0.5px;
  }
  .brand-square {
    width: 40px;
    height: 40px;
    background: var(--white);
  }
  .rule {
    position: absolute;
    left: 72px;
    right: 38px;
    top: 139px;
    height: 1px;
    background: var(--white);
    opacity: 0.85;
  }
  .tagline {
    position: absolute;
    right: 38px;
    top: 150px;
    font-weight: 500;
    font-size: 15px;
    line-height: 1;
    letter-spacing: 0.3px;
  }
</style>
</head>
<body>
  <div class="canvas">
    <header class="banner">
      <div class="decor decor-left" role="img" aria-label="Decorative white cloud shapes along the left edge"></div>
      <div class="decor decor-top" role="img" aria-label="Decorative outlined cloud along the top edge"></div>
      <div class="decor decor-right" role="img" aria-label="Decorative white cloud shapes along the right edge"></div>

      <div class="brand">
        <span class="brand-square"></span>
        <span class="brand-name">Lumenfield Dossiers</span>
      </div>

      <div class="rule"></div>

      <p class="tagline">The Technology Pro’s Research Hub</p>
    </header>
  </div>
</body>
</html>
```